Medical device engineering service firm needs an update to flier

We do engineering design work for medical products, from ideation through injection-molded prototypes. Our clients have assay that needs automation, or an idea that needs to be made concrete. We have a 2-sided flier that needs an update to the look. This flier is mainly used as both a take away at trade shows to describe our services and provide our contact information.

```html
<!DOCTYPE html>
<html lang="en">
<head>
<meta charset="utf-8">
<title>Veranthe Product Development – Flier</title>
<link href="https://fonts.googleapis.com/css2?family=Oswald:wght@300;400&family=Open+Sans:wght@400;600;700&display=swap" rel="stylesheet">
<style>
:root{
  --purple:#6e2a8c;
  --purple-deep:#3d1150;
  --green:#a4c23a;
  --ink:#2b2b2b;
  --grey-text:#707070;
  --band-dark:#1c1c1c;
  --col-light:#9c9c9c;
  --col-mid:#6f6f6f;
  --col-dark:#393939;
  --col-body:#ebebeb;
  --stage:#e6e2dc;
  --white:#ffffff;
}
*{box-sizing:border-box;margin:0;padding:0}
html,body{width:1200px;height:767px;overflow:hidden;background:var(--stage)}
body{position:relative;font-family:"Open Sans",Arial,sans-serif;color:var(--ink)}
.page{position:absolute;top:46px;width:518px;height:670px;background:var(--white);overflow:hidden;box-shadow:0 6px 18px rgba(0,0,0,.25)}
.page--front{left:54px}
.page--back{left:625px}
.abs{position:absolute}

/* front */
.brand{left:20px;top:26px;color:var(--purple);font-weight:600;line-height:1}
.brand__name{font-size:40px;letter-spacing:-0.5px}
.brand__sub{font-size:10px;letter-spacing:1.6px;margin-top:4px;text-transform:uppercase}
.hero-band{left:0;top:113px;width:430px;height:190px;background:linear-gradient(90deg,#141414,#3a3a3a)}
.hero-art{left:0;top:0;width:518px;height:330px}
.headline{left:16px;top:124px;font-family:"Oswald",Arial,sans-serif;font-weight:300;font-size:21px;line-height:28px;color:var(--white);text-transform:uppercase;letter-spacing:-0.3px}
.headline__lead{color:var(--green)}
.headline-rule{left:16px;top:213px;width:185px;height:1px;background:var(--green)}
.intro{left:16px;top:222px;width:248px;font-size:7.2px;line-height:9.1px;color:var(--white)}
.statement{left:0;top:328px;width:518px;text-align:center;font-size:13.4px;font-weight:600;color:var(--grey-text);line-height:18px;text-transform:uppercase}
.col{top:394px;height:212px;width:173px;background:var(--col-body)}
.col__head{position:absolute;left:0;top:0;width:100%;height:44px;color:var(--white);font-size:8.6px;font-weight:700;text-align:center;padding-top:29px;text-transform:uppercase}
.col--services{left:0}.col--services .col__head{background:var(--col-light)}
.col--capabilities{left:173px;background:#e4e4e4}.col--capabilities .col__head{background:var(--col-mid)}
.col--portfolio{left:346px;width:172px}.col--portfolio .col__head{background:var(--col-dark)}
.col__badge{position:absolute;top:-24px;left:50%;margin-left:-24px;width:48px;height:48px;border-radius:50%;background:radial-gradient(circle at 40% 35%,#fff,#dcdcdc);box-shadow:0 1px 3px rgba(0,0,0,.35);display:flex;align-items:center;justify-content:center}
.col__badge svg{width:26px;height:26px;fill:var(--purple)}
.col__list{position:absolute;left:14px;top:63px;right:8px;list-style:none;font-size:7.6px;line-height:11.8px;color:#3d3d3d}
.col__list li{padding-left:7px;position:relative}
.col__list li::before{content:"•";position:absolute;left:0}
.cert-mark{right:14px;bottom:10px;width:26px;height:26px;border-radius:50%;border:2px solid #c9c9c9}

/* footer */
.footer{left:0;top:622px;width:518px;height:48px;background:linear-gradient(90deg,#2a2a2a,#3d3d3d 60%,#2e2e2e)}
.footer__tab{position:absolute;left:0;top:-8px;width:236px;height:56px;background:linear-gradient(90deg,var(--purple-deep),var(--purple));border-top-right-radius:14px;display:flex;align-items:center;padding-left:24px;color:var(--white);font-size:19px;font-weight:700}
.footer__tab svg{width:20px;height:20px;margin-right:12px;fill:none;stroke:var(--white);stroke-width:1.8}
.footer__web{position:absolute;right:10px;top:8px;color:var(--green);font-size:10px;font-weight:700}
.footer__addr{position:absolute;right:10px;top:24px;color:var(--white);font-size:10px}

/* back */
.photo-top{left:0;top:0;width:518px;height:230px}
.step-title{left:22px;top:233px;font-family:"Oswald",Arial,sans-serif;font-weight:400;font-size:21px;color:var(--green);text-transform:uppercase}
.step-sub{left:22px;top:260px;font-family:"Oswald",Arial,sans-serif;font-weight:300;font-size:16px;color:var(--ink);text-transform:uppercase}
.step{position:absolute;width:164px;height:60px}
.step__icon{position:absolute;left:0;top:0;width:52px;height:52px;border-radius:50%;background:radial-gradient(circle at 40% 35%,#fff,#d9d9d9);box-shadow:0 1px 3px rgba(0,0,0,.35);display:flex;align-items:center;justify-content:center}
.step__icon svg{width:28px;height:28px;fill:var(--purple)}
.step__text{position:absolute;left:60px;top:5px;width:102px;font-size:6.8px;line-height:8.4px;color:#333}
</style>
</head>
<body>

<svg width="0" height="0" style="position:absolute" aria-hidden="true">
  <defs>
    <symbol id="i-gears" viewBox="0 0 32 32"><circle cx="12" cy="19" r="7"/><circle cx="22" cy="10" r="5"/><circle cx="12" cy="19" r="2.5" fill="#eee"/><circle cx="22" cy="10" r="1.8" fill="#eee"/></symbol>
    <symbol id="i-monitor" viewBox="0 0 32 32"><path d="M4 6h24v16H4zM7 9v10h18V9z" fill-rule="evenodd"/><rect x="14" y="22" width="4" height="4"/><rect x="10" y="26" width="12" height="2"/></symbol>
    <symbol id="i-book" viewBox="0 0 32 32"><path d="M8 4h14l4 4v20H8z"/><rect x="11" y="10" width="11" height="1.5" fill="#eee"/><rect x="11" y="14" width="11" height="1.5" fill="#eee"/></symbol>
    <symbol id="i-bulb" viewBox="0 0 32 32"><circle cx="16" cy="12" r="8"/><rect x="12" y="19" width="8" height="6" rx="1"/><rect x="13" y="26" width="6" height="2"/></symbol>
    <symbol id="i-target" viewBox="0 0 32 32"><circle cx="15" cy="17" r="11"/><circle cx="15" cy="17" r="7.5" fill="#eee"/><circle cx="15" cy="17" r="4.5"/><path d="M15 17L27 5" stroke="#6e2a8c" stroke-width="2"/></symbol>
    <symbol id="i-team" viewBox="0 0 32 32"><circle cx="16" cy="10" r="4"/><circle cx="8" cy="12" r="3"/><circle cx="24" cy="12" r="3"/><path d="M9 25a7 7 0 0 1 14 0z"/><path d="M2 25a6 6 0 0 1 9-5v5zM30 25a6 6 0 0 0-9-5v5z"/></symbol>
    <symbol id="i-chart" viewBox="0 0 32 32"><path d="M4 8h20v14H4zM6 10v10h16V10z" fill-rule="evenodd"/><rect x="2" y="22" width="24" height="3"/><rect x="24" y="4" width="3" height="3"/><rect x="27" y="7" width="3" height="3"/><rect x="24" y="10" width="3" height="3"/></symbol>
    <symbol id="i-draw" viewBox="0 0 32 32"><path d="M5 5h22v22H5zM7 7v18h18V7z" fill-rule="evenodd"/><path d="M10 22l2-6 10-10 4 4-10 10z"/></symbol>
    <symbol id="i-proto" viewBox="0 0 32 32"><path d="M4 6h20v18H4zM6 8v14h16V8z" fill-rule="evenodd"/><circle cx="14" cy="14" r="3"/><circle cx="24" cy="24" r="5"/></symbol>
    <symbol id="i-clip" viewBox="0 0 32 32"><path d="M7 5h18v24H7zM9 8v19h14V8z" fill-rule="evenodd"/><rect x="12" y="3" width="8" height="4"/><rect x="11" y="12" width="10" height="1.6"/><rect x="11" y="17" width="10" height="1.6"/><rect x="11" y="22" width="10" height="1.6"/></symbol>
    <symbol id="i-puzzle" viewBox="0 0 32 32"><circle cx="16" cy="16" r="10"/><circle cx="16" cy="16" r="4" fill="#eee"/><rect x="14" y="2" width="4" height="5"/><rect x="14" y="25" width="4" height="5"/><rect x="2" y="14" width="5" height="4"/><rect x="25" y="14" width="5" height="4"/></symbol>
    <symbol id="i-arm" viewBox="0 0 32 32"><rect x="6" y="25" width="14" height="4"/><path d="M12 25l2-12 10-6 2 3-9 5-1 10z"/><circle cx="14" cy="13" r="3"/><circle cx="26" cy="9" r="3"/></symbol>
    <symbol id="i-flow" viewBox="0 0 32 32"><path d="M2 10h10v12H2zM4 12v8h6v-8z" fill-rule="evenodd"/><path d="M12 15h6v-3l4 4-4 4v-3h-6z"/><path d="M22 8h8v16h-8zM24 10v12h4V10z" fill-rule="evenodd"/></symbol>
    <symbol id="i-doc" viewBox="0 0 32 32"><path d="M5 4h16v24H5zM7 6v20h12V6z" fill-rule="evenodd"/><rect x="9" y="10" width="8" height="1.6"/><rect x="9" y="14" width="8" height="1.6"/><circle cx="22" cy="20" r="5"/><circle cx="22" cy="20" r="3" fill="#eee"/><path d="M25 23l4 4" stroke="#6e2a8c" stroke-width="2.4"/></symbol>
    <symbol id="i-cert" viewBox="0 0 32 32"><path d="M4 4h20v18H4zM6 6v14h16V6z" fill-rule="evenodd"/><rect x="8" y="9" width="12" height="1.6"/><rect x="8" y="13" width="8" height="1.6"/><circle cx="22" cy="22" r="5"/><path d="M19 26l-1 5 4-2 4 2-1-5z"/></symbol>
    <symbol id="i-factory" viewBox="0 0 32 32"><path d="M3 28V14l7 4v-4l7 4v-4l7 4V6h5v22z"/><circle cx="16" cy="10" r="4" fill="#6e2a8c"/></symbol>
    <symbol id="i-stamp" viewBox="0 0 32 32"><circle cx="16" cy="7" r="4"/><rect x="14" y="10" width="4" height="8"/><path d="M8 18h16l2 5H6z"/><rect x="5" y="26" width="22" height="2"/></symbol>
    <symbol id="i-phone" viewBox="0 0 24 24"><circle cx="12" cy="12" r="10.5"/><path d="M8.5 6.5l2 2.2-1.2 1.6a8 8 0 0 0 4.4 4.4l1.6-1.2 2.2 2-1.2 2.2C11 17.5 6.5 13 6.3 7.7z"/></symbol>
  </defs>
</svg>

<!-- FRONT -->
<section class="page page--front">
  <div class="abs hero-band"></div>
  <svg class="abs hero-art" viewBox="0 0 518 330">
    <defs>
      <radialGradient id="heroTone" cx="55%" cy="40%" r="65%">
        <stop offset="0" stop-color="#c7d7e8"/>
        <stop offset=".55" stop-color="#6e8fb3"/>
        <stop offset="1" stop-color="#2a3f5a"/>
      </radialGradient>
    </defs>
    <path d="M0 300 Q260 330 518 250 L518 262 Q260 345 0 312 Z" fill="var(--purple)"/>
    <circle cx="430" cy="140" r="168" fill="none" stroke="var(--purple)" stroke-width="9"/>
    <circle cx="430" cy="140" r="176" fill="none" stroke="#d9d9d9" stroke-width="3"/>
    <circle cx="430" cy="140" r="160" fill="url(#heroTone)" role="img" aria-label="Photo of a scientist in a lab coat working with a digital interface"/>
  </svg>
  <div class="abs brand"><div class="brand__name">Veranthe</div><div class="brand__sub">Product Development</div></div>
  <div class="abs headline"><div class="headline__lead">Rapid Design Engineering</div><div>of Medical Devices</div><div>Specializing in Plastics</div></div>
  <div class="abs headline-rule"></div>
  <p class="abs intro">Our highly experienced biomedical and mechanical engineers leverage our extensive in-house fabrication capabilities to create proven, manufacturable designs with unmatched speed, efficiency and quality. They have developed over 300 successful designs, forming our deep portfolio that has generated hundreds of millions of dollars for our clients. It includes FDA Class I, II, and III devices, developed under our ISO 13485 certified quality management system.</p>
  <p class="abs statement">We specialize in design engineering and design for manufacturing<br>of innovative medical and life science devices that use plastics</p>

  <div class="abs col col--services">
    <div class="col__head">Our services include</div>
    <div class="col__badge"><svg><use href="#i-gears"/></svg></div>
    <ul class="col__list">
      <li>Concept Development</li><li>Engineering and Design</li><li>Industrial Design</li><li>Design for Manufacturing and Assembly</li><li>Design Control per ISO 13485</li><li>Finite Element Analysis (FEA)</li><li>Design Verification Testing</li><li>Test Method Development</li><li>Test and Assembly Fixture development</li><li>Transfer to Manufacturing</li>
    </ul>
  </div>
  <div class="abs col col--capabilities">
    <div class="col__head">Our in-house capabilities include</div>
    <div class="col__badge"><svg><use href="#i-monitor"/></svg></div>
    <ul class="col__list">
      <li>Stereolithography (SLA) Prototyping</li><li>CNC Machining / Fabrication</li><li>Prototype Mold Fabrication</li><li>Prototype Injection Molding</li><li>Liquid Injection Molded (LIM) Silicone Prototype Molding</li><li>Injection Molding Simulation and Analysis</li><li>Product Reliability Testing</li><li>Plastics Assembly Expertise</li><li>Material Selection Expertise, Research and Testing</li>
    </ul>
  </div>
  <div class="abs col col--portfolio">
    <div class="col__head">Our portfolio include</div>
    <div class="col__badge"><svg><use href="#i-book"/></svg></div>
    <ul class="col__list">
      <li>Diagnostics/Molecular Diagnostics</li><li>Sample Collection/Preparation</li><li>Life Science/Laboratory Products</li><li>Microfluidics/Small Volume Handling</li><li>Buffer &amp; Reagent Storage &amp; Delivery</li><li>Surgical/Clinical Tools</li><li>Drug Delivery Devices</li><li>Electromechanical Devices</li><li>Consumer &amp; Industrial Products</li>
    </ul>
    <div class="abs cert-mark"></div>
  </div>

  <footer class="abs footer">
    <div class="footer__tab"><svg viewBox="0 0 24 24"><use href="#i-phone"/></svg>+1 555 014 2290</div>
    <div class="footer__web">www.veranthepd.com</div>
    <div class="footer__addr">1450 Harbor View Rd. Oceanside, CA 92054</div>
  </footer>
</section>

<!-- BACK -->
<section class="page page--back">
  <svg class="abs photo-top" viewBox="0 0 518 230">
    <defs>
      <linearGradient id="backTone" x1="0" y1="0" x2="1" y2="1">
        <stop offset="0" stop-color="#5c86b5"/>
        <stop offset=".5" stop-color="#2c4f7a"/>
        <stop offset="1" stop-color="#7b6aa8"/>
      </linearGradient>
      <radialGradient id="deviceTone" cx="50%" cy="45%" r="60%">
        <stop offset="0" stop-color="#ffffff"/>
        <stop offset="1" stop-color="#c9cdd4"/>
      </radialGradient>
    </defs>
    <path d="M0 0H518V185Q260 225 0 182Z" fill="url(#backTone)" role="img" aria-label="Photo of a clinician using a tablet with medical data graphics"/>
    <path d="M0 182Q260 225 518 185V197Q260 240 0 194Z" fill="var(--purple)"/>
    <circle cx="335" cy="226" r="48" fill="#bdbdbd"/>
    <circle cx="335" cy="226" r="43" fill="url(#deviceTone)" role="img" aria-label="Photo of a small medical device component"/>
    <circle cx="452" cy="216" r="53" fill="#bdbdbd"/>
    <circle cx="452" cy="216" r="48" fill="url(#deviceTone)" role="img" aria-label="Photo of an assembled medical device prototype"/>
  </svg>
  <h2 class="abs step-title">Step to success</h2>
  <h3 class="abs step-sub">Our medical device development process</h3>

  <div class="step" style="left:25px;top:288px"><div class="step__icon"><svg><use href="#i-bulb"/></svg></div><p class="step__text">Discuss your project needs. Estimate the work to accomplish your vision.</p></div>
  <div class="step" style="left:189px;top:288px"><div class="step__icon"><svg><use href="#i-target"/></svg></div><p class="step__text">Define the product requirements, giving us a well-defined target for development.</p></div>
  <div class="step" style="left:353px;top:288px"><div class="step__icon"><svg><use href="#i-team"/></svg></div><p class="step__text">Brainstorm solutions, drawing from the experience of our entire engineering team.</p></div>

  <div class="step" style="left:25px;top:356px"><div class="step__icon"><svg><use href="#i-gears"/></svg></div><p class="step__text">Develop concepts that provide an array of potential design solutions.</p></div>
  <div class="step" style="left:189px;top:356px"><div class="step__icon"><svg><use href="#i-chart"/></svg></div><p class="step__text">Analyze and present concepts. Determine which one best meets all product requirements.</p></div>
  <div class="step" style="left:353px;top:356px"><div class="step__icon"><svg><use href="#i-draw"/></svg></div><p class="step__text">Design all details in 3D CAD, defining tolerances, materials and assembly methods.</p></div>

  <div class="step" style="left:25px;top:423px"><div class="step__icon"><svg><use href="#i-proto"/></svg></div><p class="step__text">Individual prototype any functions that are likely to require iteration.</p></div>
  <div class="step" style="left:189px;top:423px"><div class="step__icon"><svg><use href="#i-clip"/></svg></div><p class="step__text">Test prototypes against requirements. Quickly iterate with in-house prototyping.</p></div>
  <div class="step" style="left:353px;top:423px"><div class="step__icon"><svg><use href="#i-puzzle"/></svg></div><p class="step__text">Develop integrated prototype that combines all functions, and meets requirements.</p></div>

  <div class="step" style="left:25px;top:490px"><div class="step__icon"><svg><use href="#i-arm"/></svg></div><p class="step__text">Fabricate prototype tooling in-house that we can easily iterate as needed.</p></div>
  <div class="step" style="left:189px;top:490px"><div class="step__icon"><svg><use href="#i-flow"/></svg></div><p class="step__text">Mold and assemble fully functional, production quality devices.</p></div>
  <div class="step" style="left:353px;top:490px"><div class="step__icon"><svg><use href="#i-doc"/></svg></div><p class="step__text">Test molded devices against requirements. Iterate molds as needed.</p></div>

  <div class="step" style="left:25px;top:558px"><div class="step__icon"><svg><use href="#i-cert"/></svg></div><p class="step__text">Perform Design Verification Testing to confirming that all design requirements are met.</p></div>
  <div class="step" style="left:189px;top:558px"><div class="step__icon"><svg><use href="#i-factory"/></svg></div><p class="step__text">Seamlessly transfer to manufacturing for production scale up.</p></div>
  <div class="step" style="left:353px;top:558px"><div class="step__icon"><svg><use href="#i-stamp"/></svg></div><p class="step__text">Support patent and regulatory approval processes.</p></div>

  <footer class="abs footer">
    <div class="footer__tab"><svg viewBox="0 0 24 24"><use href="#i-phone"/></svg>+1 555 014 2290</div>
    <div class="footer__web">www.veranthepd.com</div>
    <div class="footer__addr">1450 Harbor View Rd. Oceanside, CA 92054</div>
  </footer>
</section>

</body>
</html>
```